Managed Service Provider need new business cards

We are a small Maanged Service Provider of IT Services and need a new fresh design for our business cards. We want something impossible, fun and professional :)
Our services has a large range, but we are always fun and make sure our customers both get their issue sorted and also feel like they are "catching up with an old friend".
All our cards in the past has always been all black, with red and we need something fresher.
The back of card, we would like just a small list of what we do i think, but if someone has a better idea, please do something cool with the back of the card:
Managed IT Services
Productivity Solutions
Data Backup and Recovery
IT System Maintenance
Managed IT Security
More details can be found on our website tqnetworks.com.au
Industry/Entity Type
It Company
Contact Information for Business Card
Name: Dwayne Falstrup
Title: Director
Phone: 03 6193 4827
Mobile: 0412 587 239
Email: dwayne@tqnetworks.com.au
Web: www.tqnetworks.com.au

```html
<!DOCTYPE html>
<html lang="en">
<head>
<meta charset="UTF-8">
<title>TQ Networks – Business Card</title>
<link href="https://fonts.googleapis.com/css2?family=Montserrat:wght@400;600&family=Oswald:wght@500&display=swap" rel="stylesheet">
<style>
  :root {
    --page-bg: #1c1c1c;
    --card-bg: #262626;
    --card-bg-light: #2e2e2e;
    --accent-red: #e3191f;
    --text-white: #f2f2f2;
    --text-grey: #cfcfcf;
  }
  * { box-sizing: border-box; margin: 0; padding: 0; }
  html, body {
    width: 1200px; height: 900px; overflow: hidden;
    background: var(--page-bg);
  }
  .canvas {
    width: 1200px; height: 900px;
    display: flex; flex-direction: column; align-items: center; justify-content: center;
    gap: 40px;
  }
  .card {
    position: relative;
    width: 660px; height: 377px;
    background: linear-gradient(135deg, var(--card-bg-light), var(--card-bg));
    box-shadow: 0 14px 30px rgba(0,0,0,0.55);
    overflow: hidden;
  }
  .card__band {
    position: absolute; left: 0; right: 0; bottom: 0;
    height: 6px; background: var(--accent-red);
  }

  /* Front */
  .brand {
    position: absolute; top: 112px; left: 0; right: 0;
    text-align: center;
    font-family: 'Montserrat', sans-serif;
    font-weight: 600;
    font-size: 46px;
    letter-spacing: 2px;
    color: var(--text-grey);
    text-transform: uppercase;
  }
  .services {
    position: absolute; left: 0; right: 0; bottom: 42px;
    text-align: center;
    font-family: 'Montserrat', sans-serif;
    font-weight: 600;
    font-size: 15px;
    line-height: 1.55;
    color: var(--text-white);
  }
  .services__sep { color: var(--accent-red); margin: 0 6px; }

  /* Back */
  .identity {
    position: absolute; top: 150px; left: 80px;
    width: 250px; text-align: right;
  }
  .identity__name {
    font-family: 'Oswald', sans-serif;
    font-weight: 500;
    font-size: 34px;
    line-height: 1;
    color: var(--accent-red);
    text-transform: uppercase;
    letter-spacing: 0.5px;
  }
  .identity__title {
    margin-top: 8px;
    font-family: 'Montserrat', sans-serif;
    font-size: 17px;
    color: var(--text-white);
  }
  .divider {
    position: absolute; top: 138px; left: 352px;
    width: 2px; height: 92px; background: var(--accent-red);
  }
  .contacts {
    position: absolute; top: 140px; left: 378px;
    list-style: none;
    font-family: 'Montserrat', sans-serif;
    font-size: 16px;
    color: var(--text-white);
  }
  .contacts__item {
    display: flex; align-items: center; gap: 10px;
    height: 23px;
  }
  .contacts__icon { width: 12px; height: 12px; flex: none; }
</style>
</head>
<body>
<main class="canvas">

  <section class="card card--front">
    <div class="brand">TQ Networks</div>
    <p class="services">
      Managed IT Services<span class="services__sep">|</span>Productivity Solutions<br>
      Data Backup and Recovery<span class="services__sep">|</span>IT System Maintenance<span class="services__sep">|</span>Managed IT Security
    </p>
    <div class="card__band"></div>
  </section>

  <section class="card card--back">
    <div class="identity">
      <h1 class="identity__name">Dwayne Falstrup</h1>
      <p class="identity__title">Director</p>
    </div>
    <div class="divider"></div>
    <ul class="contacts">
      <li class="contacts__item">
        <svg class="contacts__icon" viewBox="0 0 12 12" aria-hidden="true">
          <path d="M3 1 L4.6 3.4 L3.6 4.6 Q4.6 6.8 7.2 8.2 L8.4 7.2 L11 8.8 L10 11 Q4 11 1 3 Z" fill="none" stroke="var(--accent-red)" stroke-width="1.2" stroke-linejoin="round"/>
        </svg>
        <span>03 6193 4827</span>
      </li>
      <li class="contacts__item">
        <svg class="contacts__icon" viewBox="0 0 12 12" aria-hidden="true">
          <rect x="3" y="0.8" width="6" height="10.4" rx="1" fill="none" stroke="var(--accent-red)" stroke-width="1.2"/>
          <line x1="5" y1="9.4" x2="7" y2="9.4" stroke="var(--accent-red)" stroke-width="1"/>
        </svg>
        <span>0412 587 239</span>
      </li>
      <li class="contacts__item">
        <svg class="contacts__icon" viewBox="0 0 12 12" aria-hidden="true">
          <rect x="0.8" y="2.5" width="10.4" height="7" fill="none" stroke="var(--accent-red)" stroke-width="1.2"/>
          <path d="M0.8 2.5 L6 6.5 L11.2 2.5" fill="none" stroke="var(--accent-red)" stroke-width="1.2"/>
        </svg>
        <span>dwayne@tqnetworks.com.au</span>
      </li>
      <li class="contacts__item">
        <svg class="contacts__icon" viewBox="0 0 12 12" aria-hidden="true">
          <circle cx="6" cy="6" r="5" fill="none" stroke="var(--accent-red)" stroke-width="1.1"/>
          <ellipse cx="6" cy="6" rx="2.2" ry="5" fill="none" stroke="var(--accent-red)" stroke-width="1"/>
          <line x1="1" y1="6" x2="11" y2="6" stroke="var(--accent-red)" stroke-width="1"/>
        </svg>
        <span>www.tqnetworks.com.au</span>
      </li>
    </ul>
    <div class="card__band"></div>
  </section>

</main>
</body>
</html>
```